Accounting & Tax Services in Edmonton, Canada-Needs Website Design & Improvement

I am starting my business for accounting and tax services in Canada. I have my website but not much happy with that. My services are for bookkeeping, accounting and tax services. We serve both individual and corporate clients. I am trying to bring new idea in the market for providing services at their facility or business. My existing website is www.kvrm.ca
Currently, this site is static but I want to improve it to dynamic or interactive in nature.

Target Market(s)

Edmonton and Surrounding Areas, Canada

Industry/Entity Type

Public Accounting

Logo Text

Lakeshore Ledger & Office Partners

Number of Pages Required

4 page

Font styles to use
Sans Serif

Colors

Designer to choose colors to be used in the design.

Requirements
Must have
• 4 Pages
• I a not sure what do we mean by coded and uncoded design. Need clarification
• Rest is explained in project description. It should have the ingredients to attract traffic in any professional website.
• Logo Design Text can be shortened, if required.
• Existing logo attached, just for reference.
Nice to have
• 5 Pages

```html
<!DOCTYPE html>
<html lang="en">
<head>
<meta charset="utf-8">
<title>Lakeshore Ledger &amp; Office Partners – Accounting &amp; Tax Services in Edmonton</title>
<link href="https://fonts.googleapis.com/css2?family=Open+Sans:ital,wght@0,400;0,600;0,700;1,400&family=Raleway:wght@500;600;700;800&display=swap" rel="stylesheet">
<style>
:root{
  --navy:#1f4f69;
  --nav:#2a5f7a;
  --band:#0f5a7f;
  --teal:#4c97ad;
  --sky:#0ea5e4;
  --ink:#2b2b2b;
  --text:#555;
  --muted:#888;
  --page:#e8e8e8;
  --white:#fff;
  --footer:#3a3a3a;
  --bottom:#232323;
}
*{box-sizing:border-box;margin:0;padding:0}
html,body{width:1200px;height:2699px;overflow:hidden}
body{position:relative;background:var(--page);font-family:"Open Sans",Arial,sans-serif;color:var(--text)}
.abs{position:absolute}

/* header */
.site-header{position:absolute;left:0;top:0;width:1200px;height:108px;background:#efefef;border-top:4px solid var(--nav)}
.brand{position:absolute;left:65px;top:26px;display:flex;align-items:center;gap:12px}
.brand-mark{width:26px;height:26px;background:var(--nav)}
.brand-name{font-family:"Open Sans",sans-serif;font-weight:600;font-size:21px;color:var(--nav);line-height:1.15;width:270px}
.contact-bar{position:absolute;right:50px;top:40px;display:flex;gap:34px;font-size:15px;color:#333}
.contact-bar span{display:flex;align-items:center;gap:8px}

.main-nav{position:absolute;left:0;top:108px;width:1200px;height:50px;background:var(--nav)}
.main-nav a{position:absolute;top:16px;color:var(--white);text-decoration:none;font-size:14px;letter-spacing:.2px}
.main-nav a.active::after{content:"";position:absolute;left:-12px;right:-12px;top:28px;height:3px;background:#7fb3c8}

/* hero */
.hero{position:absolute;left:0;top:158px;width:1200px;height:607px;background:linear-gradient(120deg,#0f1e2b 0%,#2d4a63 35%,#6d8499 60%,#2a3848 100%)}
.hero-kicker{position:absolute;left:0;width:1200px;top:232px;text-align:center;font-family:"Raleway",sans-serif;font-weight:700;font-size:19px;color:var(--white);letter-spacing:.5px}
.hero-title{position:absolute;left:0;width:1200px;top:260px;text-align:center;font-family:"Raleway",sans-serif;font-weight:800;font-size:44px;color:var(--white);letter-spacing:1px}
.btn-dark{display:inline-block;background:var(--nav);color:var(--white);font-family:"Raleway",sans-serif;font-weight:600;font-size:15px;padding:11px 18px;border-radius:4px}
.hero .btn-dark{position:absolute;left:546px;top:325px}

/* intro */
.intro{position:absolute;left:67px;top:716px;width:1066px;height:342px;background:var(--white);border-top:4px solid #8fc6d4;text-align:center}
.intro-rule{position:absolute;left:107px;right:50px;top:48px;height:1px;background:#bbb}
.intro h1{position:absolute;left:0;width:100%;top:82px;font-family:"Raleway",sans-serif;font-weight:700;font-size:34px;color:var(--ink)}
.intro p{position:absolute;left:70px;width:926px;font-size:14.5px;line-height:23px;color:#555}

/* services */
.what-we-do{position:absolute;left:67px;top:1115px;width:250px}
.what-we-do h2{font-family:"Raleway",sans-serif;font-weight:700;font-size:31px;color:var(--nav)}
.what-we-do p{font-size:14.5px;line-height:23px;color:#444;margin-top:6px}
.what-we-do .btn-dark{margin-top:20px}
.service{position:absolute;top:1117px;width:243px}
.service .photo{height:171px;width:100%}
.service h3{font-family:"Raleway",sans-serif;font-weight:700;font-size:19.5px;color:#222;margin-top:13px}
.service p{font-size:14px;line-height:21px;color:#666;margin-top:6px;height:72px}
.service a{font-size:12.5px;font-weight:700;color:var(--nav);text-decoration:none}

/* glance band */
.glance{position:absolute;left:0;top:1527px;width:1200px;height:395px;background:var(--band)}
.glance-photo{position:absolute;left:504px;top:0;width:696px;height:395px;background:linear-gradient(115deg,#dfe8ec 0%,#a8bcc6 45%,#3b4a58 75%,#d0d8de 100%);clip-path:polygon(0 50%,95px 0,100% 0,100% 100%,95px 100%)}
.glance h2{position:absolute;left:67px;top:55px;font-family:"Raleway",sans-serif;font-weight:800;font-size:29px;color:var(--white)}
.glance h4{position:absolute;left:67px;top:109px;font-family:Georgia,"Times New Roman",serif;font-weight:700;font-size:16px;color:var(--white)}
.glance p{position:absolute;left:67px;width:395px;font-size:15px;line-height:22px;color:var(--white)}
.glance .btn{position:absolute;top:270px;height:38px;font-size:13px;padding:10px 12px}
.btn-sky{left:67px;width:160px;background:var(--sky);color:#d7f0ff}
.btn-white{left:237px;width:102px;background:var(--white);color:#555}
.dots{position:absolute;left:157px;top:329px;display:flex;gap:10px}
.dots i{width:13px;height:13px;background:#3ab3ea;transform:rotate(45deg)}
.dots i.on{background:var(--white)}

/* reviews */
.reviews-title{position:absolute;left:65px;top:2085px;font-family:"Raleway",sans-serif;line-height:30px}
.reviews-title .a{font-weight:500;font-size:26px;color:var(--nav)}
.reviews-title .b{font-weight:800;font-size:27px;color:#1c4e8a;display:block}
.reviews-rule{position:absolute;left:293px;top:1980px;width:1px;height:270px;background:#c8c8c8}
.quote-badge{position:absolute;left:264px;top:2088px;width:58px;height:58px;border-radius:50%;background:var(--white)}
.avatar{position:absolute;left:698px;top:1982px;width:68px;height:76px}
.quote{position:absolute;left:370px;width:764px;top:2089px;text-align:center;font-style:italic;font-size:17px;line-height:31px;color:#777}
.cite{position:absolute;left:370px;width:764px;top:2193px;text-align:center;font-style:italic;font-size:11.5px;color:#888}
.arrow{position:absolute;top:2096px;font-size:18px;color:#fff}

/* footer */
.site-footer{position:absolute;left:0;top:2310px;width:1200px;height:342px;background:var(--footer)}
.quick-links h5{position:absolute;left:65px;top:108px;font-family:"Raleway",sans-serif;font-weight:700;font-size:17px;color:var(--white)}
.quick-links .rule{position:absolute;left:65px;top:136px;width:201px;height:2px;background:var(--white)}
.quick-links ul{position:absolute;top:172px;list-style:none}
.quick-links li{font-size:14.5px;color:var(--white);height:32px;display:flex;align-items:center;gap:7px}
.quick-links li::before{content:"";width:7px;height:7px;border-radius:50%;background:var(--white)}
.signup{position:absolute;left:495px;top:50px;width:705px;height:292px;background:var(--white)}
.signup h5{position:absolute;left:79px;top:45px;font-family:"Raleway",sans-serif;font-weight:700;font-size:18px;color:#222;letter-spacing:.3px}
.signup p{position:absolute;left:84px;width:560px;top:72px;font-size:12.5px;line-height:19px;color:#666}
.signup h6{position:absolute;left:90px;top:138px;font-family:"Raleway",sans-serif;font-weight:700;font-size:18px;color:#333}
.signup .field{position:absolute;left:86px;top:183px;width:359px;height:49px;background:#e6e6e6;border:1px solid #d0d0d0;font-style:italic;font-size:11px;color:#777;padding:17px 14px}
.signup .go{position:absolute;left:462px;top:183px;width:114px;height:49px;background:var(--teal);color:var(--white);font-weight:700;font-size:13px;text-align:center;line-height:49px}
.diamond{position:absolute;left:423px;top:2448px;width:144px;height:122px}
.copyright{position:absolute;left:0;top:2652px;width:1200px;height:47px;background:var(--bottom);color:var(--white);text-align:center;font-size:13px;line-height:47px}
</style>
</head>
<body>

<header class="site-header">
  <div class="brand"><span class="brand-mark"></span><span class="brand-name">Lakeshore Ledger &amp; Office Partners</span></div>
  <div class="contact-bar">
    <span><svg width="20" height="20" viewBox="0 0 20 20"><circle cx="10" cy="10" r="9" fill="#222"/><path d="M6 7c1 3 3 5 7 7l1-2-2-1-1 1c-1-1-2-2-3-3l1-1-1-2z" fill="#fff"/></svg>+(587) 555 0142</span>
    <span><svg width="22" height="16" viewBox="0 0 22 16"><rect x="1" y="1" width="20" height="14" fill="none" stroke="#333" stroke-width="1.5"/><path d="M1 1l10 8 10-8" fill="none" stroke="#333" stroke-width="1.5"/></svg>accountingservices@kvrm.ca</span>
  </div>
</header>

<nav class="main-nav">
  <a class="active" style="left:84px">HOME</a>
  <a style="left:214px">FIRM PROFILE</a>
  <a style="left:342px">CLIENT SERVICES</a>
  <a style="left:518px">NEWSLETTERS</a>
  <a style="left:675px">FINANCIAL TOOLS</a>
  <a style="left:857px">INFO CENTRE</a>
  <a style="left:1010px">CONTACT US</a>
</nav>

<section class="hero" role="img" aria-label="Photo of advisers reviewing financial charts on a laptop in an office">
  <div class="hero-kicker">CONSULTING / FINANCIAL / ECONOMICS</div>
  <div class="hero-title">FINANCIAL ADVISER</div>
  <span class="btn-dark">Read More</span>
</section>

<section class="intro">
  <div class="intro-rule"></div>
  <h1>Accounting &amp; Tax Services in Edmonton</h1>
  <p style="top:144px">Welcome and thank you for visiting our website. At Lakeshore Ledger &amp; Office Partners, we have built our business so that it guarantees your success. In addition to providing you with a profile of our firm and the services we provide, this website has been designed to become a helpful resource tool to you, our valued clients and visitors.</p>
  <p style="top:236px">Our firm endeavors to provide you with the highest quality of service and we hope that you find the information on this website useful. For any additional questions or comments please do not hesitate to contact us. We will get back to you as soon as possible as we pride ourselves on being proactive and responsive to our clients' inquiries and suggestions.</p>
</section>

<section class="what-we-do">
  <h2>What We Do</h2>
  <p>At Northgate Advisory, we focus on our our clients' most critical issues and thats greates opportunities.</p>
  <p style="margin-top:18px">Generally, the services we offer and involve preparing a financial plan or rendering financial consultation financial consultatio financial consultatio for client based on the client's</p>
  <span class="btn-dark">Read More</span>
</section>

<article class="service" style="left:347px">
  <div class="photo" role="img" aria-label="Photo of colleagues discussing documents at a desk" style="background:linear-gradient(135deg,#eef1f4,#b9c3cc)"></div>
  <h3>Accounting Solutions</h3>
  <p>Our firm offers a wide range of services to our individual and business clients. Our clients.</p>
  <a>Learn More &gt;</a>
</article>
<article class="service" style="left:619px">
  <div class="photo" role="img" aria-label="Photo of a team meeting around a table from above" style="background:linear-gradient(135deg,#4b6f8f,#d8b47a 55%,#2e3d4c)"></div>
  <h3>Tax Services</h3>
  <p>In order to guarantee our clients' success, we believe that it is necessary to provide</p>
  <a>Learn More &gt;</a>
</article>
<article class="service" style="left:883px">
  <div class="photo" role="img" aria-label="Photo of two business people reviewing papers" style="background:linear-gradient(135deg,#f3f3f3,#c4c9cf)"></div>
  <h3>Business Solutions</h3>
  <p>Our team recognizes how difficult it is to stay up-to-date on the dynamic tax laws</p>
  <a>Learn More &gt;</a>
</article>

<section class="glance">
  <div class="glance-photo" role="img" aria-label="Photo of two businessmen in suits at a meeting"></div>
  <h2>COMPANY AT A GLANCE</h2>
  <h4>Support For Financial Interest</h4>
  <p style="top:133px">At Northgate Advisory, we focus on our our clients' most critical issues and thats greates opportunities.</p>
  <p style="top:193px">Generally, the services we offer and involve preparing a financial plan or rendering financial consultation financial consultatio financial.</p>
  <span class="btn btn-sky">ℹ Explore Our Service</span>
  <span class="btn btn-white">ℹ More Info</span>
  <div class="dots"><i></i><i class="on"></i><i></i><i></i></div>
</section>

<section class="reviews">
  <div class="reviews-title"><span class="a">Coustomers</span><span class="b">REVIEWS</span></div>
  <div class="reviews-rule"></div>
  <div class="quote-badge"><svg width="58" height="58" viewBox="0 0 58 58"><path d="M21 25h6v8h-6zM31 25h6v8h-6zM23 25l2-4M33 25l2-4" stroke="#333" stroke-width="2" fill="#333"/></svg></div>
  <svg class="avatar" viewBox="0 0 68 76" role="img" aria-label="Reviewer portrait"><polygon points="34,0 68,19 68,57 34,76 0,57 0,19" fill="#cfd4d8"/><polygon points="34,6 62,22 62,54 34,70 6,54 6,22" fill="#8a9199"/></svg>
  <span class="arrow" style="left:352px">←</span>
  <p class="quote">"The benefits of psychological capital appear to be as central to the success of entrepreneurs as more traditional forms of capital."</p>
  <span class="arrow" style="left:1118px">→</span>
  <p class="cite">("The Role of Affect in the Entrepreneurial Process," M.T. Hollis, The Journal of Venture Studies, Vol. 33 (2).</p>
</section>

<footer class="site-footer">
  <div class="quick-links">
    <h5>Quick Links•</h5>
    <div class="rule"></div>
    <ul style="left:65px"><li>Home</li><li>About Us</li><li>Contact Us</li><li>Our Firm</li></ul>
    <ul style="left:197px"><li>Our Story</li><li>Our Services</li><li>Problems and Solutions</li><li>Group &amp; Relationship Models</li></ul>
  </div>
  <div class="signup">
    <h5>LAKESHORE LEDGER &amp; OFFICE PARTNERS</h5>
    <p>No matter how successful you are as an entrepreneur, there are always higher levels you want to achieve in both your business and personal life – two areas that are inseparable and continuously impacting each other.&nbsp; Our services are transformative.</p>
    <h6>Sign up for updates</h6>
    <div class="field">Enter Your Email Address</div>
    <div class="go">GO</div>
  </div>
</footer>
<svg class="diamond" viewBox="0 0 144 122">
  <polygon points="0,61 72,0 72,122" fill="#fff"/>
  <polygon points="72,0 144,61 72,122" fill="#111"/>
  <g fill="none" stroke="#111" stroke-width="3" stroke-linecap="round">
    <path d="M38 66l-4 4a5 5 0 0 0 7 7l6-6a5 5 0 0 0 0-7"/>
    <path d="M54 56l4-4a5 5 0 0 0-7-7l-6 6a5 5 0 0 0 0 7"/>
    <path d="M42 68l10-10"/>
  </g>
  <g fill="none" stroke="#fff" stroke-width="3" stroke-linecap="round">
    <path d="M88 55h16l-4-4M104 67H88l4 4"/>
  </g>
</svg>
<div class="copyright">Copyright 2017 - All Rights Reserved</div>

</body>
</html>
```